Heritage Hollow Business Cards

Require a business card design. <br/><br/>Needs to include logo (either round or long version) plus these details:<br/>Maya Torvel<br/>Heritage Hollow<br/>maya@quonbrook.com.au<br/>02 6481 7390<br/>PO Box Glenwarra NSW 2913<br/>www.heritagehollow.com.au<br/><br/>I need in an editable format so that I can create for multiple staff members. <br/><br/>

Target Market(s)

We are an online store selling renovation products to home owners are builders. Looking for a classic classy design.

Industry/Entity Type

Home And Garden

Contact Information for Business Card

Maya Torvel
Heritage Hollow
maya@quonbrook.com.au
02 6481 7390
PO Box Glenwarra NSW 2913
www.heritagehollow.com.au

Colors

Designer to choose colors to be used in the design.

Requirements
Must have
• Must include Logo.

```html
<!DOCTYPE html>
<html lang="en">
<head>
<meta charset="utf-8">
<title>Heritage Hollow — Business Card</title>
<link href="https://fonts.googleapis.com/css2?family=Raleway:ital,wght@0,300;0,500;1,500&display=swap" rel="stylesheet">
<style>
  :root {
    --page-bg: #fdfdfd;
    --card-bg: #ffffff;
    --card-border: #bdbdbd;
    --ink: #2f2f2f;
    --ink-soft: #3c3c3c;
    --brand-ink: #4a4a4a;
  }
  html, body {
    margin: 0;
    padding: 0;
    width: 1200px;
    height: 923px;
    overflow: hidden;
    background: var(--page-bg);
    font-family: "Raleway", sans-serif;
  }
  .canvas {
    position: relative;
    width: 1200px;
    height: 923px;
  }
  .business-card {
    position: absolute;
    left: 336px;
    top: 306px;
    width: 527px;
    height: 311px;
    box-sizing: border-box;
    border: 2px solid var(--card-border);
    background: var(--card-bg);
  }
  .brand-mark {
    position: absolute;
    left: 76px;
    top: 168px;
    margin: 0;
    font-weight: 500;
    font-size: 22px;
    line-height: 24px;
    color: var(--brand-ink);
  }
  .holder {
    position: absolute;
    left: 344px;
    top: 56px;
  }
  .holder-name {
    margin: 0;
    font-weight: 300;
    font-size: 24px;
    line-height: 28px;
    letter-spacing: 0.3px;
    color: var(--ink);
  }
  .holder-company {
    margin: 0;
    font-weight: 500;
    font-style: italic;
    font-size: 15px;
    line-height: 18px;
    color: var(--ink);
  }
  .contact-list {
    position: absolute;
    right: 32px;
    top: 214px;
    margin: 0;
    padding: 0;
    list-style: none;
    text-align: right;
    font-weight: 500;
    font-size: 15px;
    line-height: 20px;
    color: var(--ink-soft);
  }
</style>
</head>
<body>
  <main class="canvas">
    <section class="business-card" aria-label="Heritage Hollow business card">
      <p class="brand-mark">Heritage<br>Hollow</p>

      <div class="holder">
        <h1 class="holder-name">MAYA TORVEL</h1>
        <p class="holder-company">Heritage Hollow</p>
      </div>

      <ul class="contact-list">
        <li>maya@quonbrook.com.au</li>
        <li>02 6481 7390</li>
        <li>PO Box Glenwarra NSW 2913</li>
        <li>www.heritagehollow.com.au</li>
      </ul>
    </section>
  </main>
</body>
</html>
```